Corrindale Planners, LLC Stationary

Corrindale Planners, LLC is a new financial planning and consulting company. We are looking for designs on business cards, letterhead, envelopes, and anything else that would be useful. Our preference for business card design is two sided. We are looking for a professional and clean look with incorporating the logo and patriotic feel. Thank you to all who participate and good luck!

```html
<!DOCTYPE html>
<html lang="en">
<head>
<meta charset="utf-8">
<title>Corrindale Planners, LLC — Business Cards</title>
<link href="https://fonts.googleapis.com/css2?family=Open+Sans:wght@400;600;700&family=Questrial&display=swap" rel="stylesheet">
<style>
  :root {
    --backdrop: #3a3d42;
    --navy: #14275e;
    --blue: #1a4f9c;
    --blue-deep: #0b1f55;
    --blue-light: #2a7ad0;
    --red: #c4202a;
    --paper: #ffffff;
    --paper-shade: #d9dce1;
    --ink: #1c1f26;
    --band-text: #e8eefa;
  }
  * { margin: 0; padding: 0; box-sizing: border-box; }
  html, body { width: 1200px; height: 900px; overflow: hidden; }
  body {
    background: var(--backdrop);
    font-family: "Open Sans", Arial, sans-serif;
    position: relative;
  }
  .presentation-title {
    position: absolute;
    top: 26px;
    right: 96px;
    font-family: "Questrial", "Century Gothic", sans-serif;
    font-size: 50px;
    color: var(--paper);
    font-weight: 400;
    letter-spacing: 0.5px;
  }
  .card {
    position: absolute;
    width: 620px;
    height: 340px;
    border-radius: 22px;
    overflow: hidden;
    box-shadow: 0 10px 26px rgba(0,0,0,0.45);
  }
  .card--front { left: 180px; top: 150px; background: linear-gradient(135deg, var(--paper-shade) 0%, var(--paper) 45%, #eef0f3 100%); }
  .card--back { left: 180px; top: 525px; background: radial-gradient(ellipse at 62% 40%, var(--blue-light) 0%, var(--blue) 40%, var(--blue-deep) 100%); }

  .brand { position: absolute; display: flex; align-items: center; gap: 12px; }
  .brand__mark { width: 34px; height: 34px; border-radius: 50%; flex: none; }
  .brand__name { font-weight: 700; font-size: 26px; letter-spacing: 1px; line-height: 1; }
  .brand__tagline { font-weight: 600; font-size: 9.5px; letter-spacing: 1.6px; margin-top: 6px; }

  .card--front .brand { left: 150px; top: 52px; }
  .card--front .brand__mark { background: var(--navy); }
  .card--front .brand__name { color: var(--navy); }
  .card--front .brand__tagline { color: var(--red); }

  .holder { position: absolute; left: 250px; top: 128px; color: var(--ink); }
  .holder__name { font-weight: 700; font-size: 17px; }
  .holder__role { font-size: 12px; margin-top: 2px; }
  .holder__contact { font-size: 13px; margin-top: 24px; line-height: 1.4; }
  .holder__contact b { font-weight: 700; }

  .band-rule { position: absolute; left: 0; right: 0; top: 232px; height: 5px; background: var(--red); }
  .band {
    position: absolute; left: 0; right: 0; top: 237px; bottom: 0;
    background: linear-gradient(90deg, var(--blue-deep) 0%, var(--blue) 55%, var(--blue-deep) 100%);
    color: var(--band-text);
    padding: 24px 0 0 250px;
    font-size: 14px;
    line-height: 1.45;
  }
  .band b { font-weight: 700; }

  .card--back .brand { left: 110px; top: 112px; }
  .card--back .brand__mark { background: var(--paper); width: 46px; height: 46px; }
  .card--back .brand__name { color: var(--paper); font-size: 38px; }
  .card--back .brand__tagline { color: var(--band-text); font-size: 12px; }
  .web { position: absolute; left: 200px; top: 258px; color: var(--paper); font-size: 16px; }

  .thumb { position: absolute; left: 918px; width: 205px; height: 113px; }
  .thumb--back { top: 104px; }
  .thumb--front { top: 238px; }
  .thumb .card { left: 0; top: 0; transform: scale(0.33); transform-origin: 0 0; box-shadow: none; border-radius: 26px; }
</style>
</head>
<body>
  <h1 class="presentation-title">Corrindale Planners, LLC</h1>

  <section class="card card--front" aria-label="Business card front">
    <div class="brand">
      <span class="brand__mark"></span>
      <div>
        <div class="brand__name">CORRINDALE PLANNERS, LLC</div>
        <div class="brand__tagline">FINANCIAL PLANNING AND CONSULTING</div>
      </div>
    </div>
    <div class="holder">
      <div class="holder__name">Dana Whitfield</div>
      <div class="holder__role">President</div>
      <div class="holder__contact">dwhitfield@corrindale_planners.com<br><b>M:</b> 01-555-210-4471</div>
    </div>
    <div class="band-rule"></div>
    <div class="band">1840 Harbor Ridge Road Atlanta, GA 30309<br><b>P:</b> 404-555-0190 | <b>F:</b> 404-555-0191</div>
  </section>

  <section class="card card--back" aria-label="Business card back">
    <div class="brand">
      <span class="brand__mark"></span>
      <div>
        <div class="brand__name">CORRINDALE PLANNERS, LLC</div>
        <div class="brand__tagline">FINANCIAL PLANNING AND CONSULTING</div>
      </div>
    </div>
    <div class="web">www.corrindale_planners.com</div>
  </section>

  <div class="thumb thumb--back" aria-hidden="true">
    <div class="card card--back">
      <div class="brand">
        <span class="brand__mark"></span>
        <div>
          <div class="brand__name">CORRINDALE PLANNERS, LLC</div>
          <div class="brand__tagline">FINANCIAL PLANNING AND CONSULTING</div>
        </div>
      </div>
      <div class="web">www.corrindale_planners.com</div>
    </div>
  </div>

  <div class="thumb thumb--front" aria-hidden="true">
    <div class="card card--front">
      <div class="brand">
        <span class="brand__mark"></span>
        <div>
          <div class="brand__name">CORRINDALE PLANNERS, LLC</div>
          <div class="brand__tagline">FINANCIAL PLANNING AND CONSULTING</div>
        </div>
      </div>
      <div class="holder">
        <div class="holder__name">Dana Whitfield</div>
        <div class="holder__role">President</div>
        <div class="holder__contact">dwhitfield@corrindale_planners.com<br><b>M:</b> 01-555-210-4471</div>
      </div>
      <div class="band-rule"></div>
      <div class="band">1840 Harbor Ridge Road Atlanta, GA 30309<br><b>P:</b> 404-555-0190 | <b>F:</b> 404-555-0191</div>
    </div>
  </div>
</body>
</html>
```